Reed & Vale NC grand opening (for BILLBOARD)

Advertising the grand opening of our cannabis/hemp shop in NC. We will sell all things hemp (flower, cartridges, disposables, edibles, creams, lotions, pet products etc...)

Requirements
Must have
• include, open starting Aug 1, but grand opening Aug 15th.
Nice to have
• Difference slogan ideas "Save some cash, buy our grass" "Find your perfect high at Reed & Vale cannabis store" "Experience Nature's Gift: Reed & Vale Cannabis Store"

```html
<!DOCTYPE html>
<html lang="en">
<head>
<meta charset="utf-8">
<title>Reed &amp; Vale — Grand Opening Billboard</title>
<link href="https://fonts.googleapis.com/css2?family=Montserrat:wght@500;600;700;800&display=swap" rel="stylesheet">
<style>
  :root {
    --leaf-green: #82c341;
    --forest-green: #026940;
    --ink-navy: #2b2c3e;
    --paper: #ffffff;
    --backdrop: #f2f2f2;
  }
  html, body {
    margin: 0;
    width: 1200px;
    height: 757px;
    overflow: hidden;
    background: var(--backdrop);
    font-family: "Montserrat", Arial, sans-serif;
  }
  .canvas {
    position: relative;
    width: 1200px;
    height: 757px;
  }
  .billboard {
    position: absolute;
    left: 0;
    top: 102px;
    width: 1285px;
    height: 592px;
    background: var(--paper);
    overflow: hidden;
    transform: scale(0.93385);
    transform-origin: top left;
  }
  .billboard__swoosh {
    position: absolute;
    inset: 0;
    width: 100%;
    height: 100%;
  }
  .brand {
    position: absolute;
    left: 111px;
    top: 280px;
    width: 460px;
  }
  .brand__name {
    display: flex;
    align-items: center;
    gap: 14px;
    margin: 0;
    font-size: 68px;
    font-weight: 600;
    color: var(--leaf-green);
    letter-spacing: -1px;
    line-height: 1;
    white-space: nowrap;
  }
  .brand__dot {
    width: 26px;
    height: 26px;
    border-radius: 50%;
    background: var(--leaf-green);
    flex: none;
  }
  .brand__tagline {
    margin: 30px 0 0;
    font-size: 26.5px;
    font-weight: 600;
    color: var(--ink-navy);
    letter-spacing: 0.2px;
    white-space: nowrap;
  }
  .dates {
    position: absolute;
    left: 764px;
    top: 74px;
    color: var(--paper);
  }
  .dates__label {
    margin: 0;
    font-size: 29px;
    font-weight: 500;
    letter-spacing: 1px;
    color: var(--ink-navy);
    line-height: 1;
    white-space: nowrap;
  }
  .dates__label--strong {
    font-weight: 700;
    font-size: 38px;
    letter-spacing: 0.5px;
    margin-top: 44px;
  }
  .dates__day {
    margin: -4px 0 0;
    font-size: 90px;
    font-weight: 800;
    line-height: 1;
    letter-spacing: 0;
    color: var(--paper);
    white-space: nowrap;
  }
  .dates__day--grand {
    margin-top: -12px;
  }
</style>
</head>
<body>
  <main class="canvas">
    <section class="billboard" aria-label="Reed &amp; Vale grand opening billboard">
      <svg class="billboard__swoosh" viewBox="0 0 1285 592" preserveAspectRatio="none" aria-hidden="true">
        <path d="M20,0 C250,40 420,110 520,200 C600,275 650,330 720,380 C850,480 1050,560 1285,592 L1285,0 Z" fill="var(--forest-green)"/>
        <path d="M186,0 C360,50 500,110 580,195 C640,260 680,300 740,345 C870,450 1060,540 1285,584 L1285,0 Z" fill="var(--leaf-green)"/>
      </svg>

      <div class="brand">
        <h1 class="brand__name"><span class="brand__dot"></span>Reed &amp; Vale</h1>
        <p class="brand__tagline">Save some cash, buy our grass</p>
      </div>

      <div class="dates">
        <p class="dates__label">OPEN STARTING</p>
        <p class="dates__day">AUG 1</p>
        <p class="dates__label dates__label--strong">BUT GRAND OPENING</p>
        <p class="dates__day dates__day--grand">AUG 15TH</p>
      </div>
    </section>
  </main>
</body>
</html>
```